Advertisement for my roofing company

Looking to get designs for:

- Secondary Logo
- Business card designs
- Small Yard Signs (like the KVL/Perch Alarm signs people put at the mail box to let bad guys know there's camera's)
- Quick Door note/flyer to leave while canvassing letting them know we are working in neighborhoods/area and want to check out their roof to see if it qualifies for roof replacement paid for by insurance.
- any other good ideas not commoningly used that is different and stands out from everyone else

We are in need of some help getting a page designed for a high school football game program packet that the school will sell to locals with all the team information in it for this years team. We are planning to do a full page for our company branding, is this something you guys can help me with? They are requesting a PDF final copy by July 1st.

Just want to advertise what we do for homeowners after a storm impacts their areas.

Basically a quick summary about our company.

We are a roofing company that specialize in storm restoration and insurance claims. Prior to the start up of vela crest me and the business partner were insurance adjuster that handle property claims after major storm event all over the country and work storm like hurricanes to snow storms that caused damage so that gives the property owner the advantage when they use us after a storm because we have over 25+ years of insurance adjusting back ground and knowledge for the major carriers people use. We also provide other services like roof repairs, gutters systems, siding, painting interior/exterior, and windows. Main focus is roofing though! We do tons of door knocking to in area that are recently impacted by storms and offer free inspections to homeowner/property owners who are concerned or curious how their roof/property held up during the storm. We also offer inspections with a Drone Inspections using SKYLOOM AI HAIL SCANNER SUITE for those people who just feel more comfortable with that. ( which is huge and helps us land lots of leads )

We proudly carry the highest residential certification with all the large roofing material manufactures. We are BRQ Sovereign Summit Select with BRQ and Ridge Keeper w/ Oakhallow which are the only two we install anymore due to the fact the rest of them are trash.

Don't use all that or anything but this just gives you a idea what we represent.

Target Market(s)

Homeowners/property owners

Industry/Entity Type

Roofing

Font styles to use
Sans Serif

Colors
EB3D1F
EC4F4E
F09395
F8D3D4
FCEDEE

Requirements
Nice to have
• Modern design look
Should not have
• Generic google/online photos.

```html
<!DOCTYPE html>
<html lang="en">
<head>
<meta charset="utf-8">
<title>Vela Crest Roofing – Storm Restoration Flyer</title>
<link href="https://fonts.googleapis.com/css2?family=Bebas+Neue&family=Poppins:wght@400;500;600;700&display=swap" rel="stylesheet">
<style>
  :root{
    --red:#e01f26;
    --red-deep:#b3151b;
    --black:#1c1c1e;
    --ink:#222;
    --white:#fff;
    --page:#d9d9d9;
    --navy:#1b2340;
  }
  *{box-sizing:border-box;margin:0;padding:0}
  html,body{width:1200px;height:2404px;overflow:hidden;background:var(--page)}
  body{font-family:"Poppins",sans-serif;color:var(--ink);position:relative}
  .flyer{position:absolute;left:40px;top:478px;width:1120px;height:1447px;background:var(--white);overflow:hidden;box-shadow:0 18px 30px rgba(0,0,0,.25)}
  .hero-photo{position:absolute;left:0;top:0;width:1120px;height:414px;
    background:linear-gradient(180deg,#141a33 0%,#2a3566 45%,#3b4a7a 60%,#5f6670 100%)}
  .hero-photo .house{position:absolute;right:0;top:110px;width:560px;height:304px;
    background:linear-gradient(160deg,#8a8f96 0%,#5b6673 50%,#4a525c 100%)}
  .brand{position:absolute;left:58px;top:70px;color:var(--white);display:flex;align-items:center;gap:14px}
  .brand-mark{width:22px;height:22px;background:var(--red)}
  .brand-name{font-weight:700;font-size:40px;line-height:1;letter-spacing:1px}
  .brand-sub{font-weight:700;font-size:40px;line-height:1;display:block;font-size:22px;letter-spacing:5px;margin-top:6px}
  .red-band{position:absolute;left:0;top:202px;width:840px;height:187px;background:var(--red);
    clip-path:polygon(0 0,100% 0,80% 100%,0 100%)}
  .black-strip{position:absolute;left:0;top:389px;width:730px;height:25px;background:var(--black);
    clip-path:polygon(0 0,100% 0,97% 100%,0 100%)}
  .kicker{position:absolute;left:60px;top:220px;color:var(--white);font-weight:600;font-size:26px;display:flex;align-items:center;gap:8px}
  .kicker::after{content:"";display:block;width:210px;height:2px;background:var(--white);margin-top:10px}
  .headline{position:absolute;left:58px;top:252px;color:var(--white);font-family:"Bebas Neue",sans-serif;font-size:66px;line-height:.9;letter-spacing:.5px}
  .intro{position:absolute;left:0;top:432px;width:1120px;height:129px;background:var(--black);color:var(--white);
    font-size:19.5px;line-height:1.14;padding:18px 330px 0 60px}
  .years-badge{position:absolute;left:842px;top:342px;width:218px;height:240px}
  .years-badge .tail{position:absolute;bottom:0;width:30px;height:26px;background:var(--red-deep)}
  .years-badge .tail.l{left:-28px;clip-path:polygon(100% 0,100% 100%,0 100%)}
  .years-badge .tail.r{right:-28px;clip-path:polygon(0 0,100% 100%,0 100%)}
  .years-shape{position:absolute;inset:0;background:var(--red);clip-path:polygon(50% 0,100% 22%,100% 100%,0 100%,0 22%)}
  .years-top{position:absolute;top:52px;width:100%;text-align:center;color:var(--white);font-size:19px}
  .years-box{position:absolute;left:6px;right:6px;top:82px;height:70px;background:var(--black);color:var(--white);
    font-family:"Bebas Neue",sans-serif;font-size:58px;text-align:center;line-height:72px}
  .years-note{position:absolute;top:158px;width:100%;text-align:center;color:var(--white);font-size:15px;line-height:1.17;padding:0 12px}
  .services-title{position:absolute;left:60px;top:574px;font-weight:700;font-size:32px;color:var(--ink)}
  .services-title span{color:var(--red)}
  .service-list{position:absolute;left:61px;top:624px;list-style:none}
  .service-list li{display:flex;align-items:center;height:62px;margin-bottom:5.5px;font-weight:500;font-size:30px}
  .service-list li:nth-child(4){margin-bottom:1px}
  .icon{width:62px;height:62px;margin-right:16px;flex:none}
  .divider{position:absolute;left:535px;top:635px;width:2px;height:320px;background:#bbb}
  .about{position:absolute;left:580px;top:650px;width:470px;font-size:20.5px;line-height:1.2}
  .about p+p{margin-top:30px}
  .about strong{color:var(--red);font-weight:600}
  .dark-foot{position:absolute;left:0;top:1075px;width:1120px;height:372px;background:var(--black)}
  .photo{position:absolute;top:984px;height:184px;border:3px solid var(--white)}
  .photo.one{left:55px;width:327px;background:linear-gradient(180deg,#8fb6e0 0%,#9aa4b0 45%,#3f8a3a 80%,#2d6e2a 100%)}
  .photo.two{left:397px;width:323px;background:linear-gradient(160deg,#3b5a2e 0%,#5d6468 45%,#4c7a3a 100%)}
  .photo.three{left:738px;width:324px;background:linear-gradient(180deg,#9aa0a0 0%,#7a5a44 55%,#8a6f52 100%)}
  .foot-text{position:absolute;left:60px;top:1184px;width:730px;color:var(--white);font-size:19px;line-height:1.17}
  .award{position:absolute;top:1196px;width:111px;height:111px}
  .award.a{left:816px}.award.b{left:947px}
  .rule{position:absolute;left:60px;top:1337px;width:1000px;height:2px;background:#888}
  .contacts{position:absolute;left:60px;top:1352px;width:1000px;display:flex;justify-content:space-between;color:var(--white);font-weight:500;font-size:27px}
  .contacts span{display:flex;align-items:center;gap:10px}
  .contacts svg{width:32px;height:32px}
</style>
</head>
<body>
<main class="flyer">
  <div class="hero-photo" role="img" aria-label="Two-storey grey sided house under a dark stormy sky with lightning">
    <div class="house"></div>
  </div>
  <div class="brand">
    <span class="brand-mark"></span>
    <div><span class="brand-name">VELA CREST</span><span class="brand-sub">ROOFING</span></div>
  </div>
  <div class="red-band"></div>
  <div class="black-strip"></div>
  <p class="kicker">WE SPECIALIZE IN</p>
  <h1 class="headline">STORM RESTORATION &amp;<br>INSURANCE CLAIMS</h1>

  <p class="intro">Prior to the start up of vela crest me and the business partner were insurance adjuster that handle property claims after major storm event all over the country and work storm like hurricanes to snow storms that caused damage so that gives the property owner the advantage when they use us after a storm</p>

  <div class="years-badge">
    <span class="tail l"></span><span class="tail r"></span>
    <div class="years-shape"></div>
    <p class="years-top">we have over</p>
    <p class="years-box">25+ YEARS</p>
    <p class="years-note">Of insurance adjusting back ground and knowledge for the major carriers people use</p>
  </div>

  <h2 class="services-title">WE ALSO PROVIDE <span>OTHER SERVICES LIKE</span></h2>
  <ul class="service-list">
    <li><svg class="icon" viewBox="0 0 62 62"><circle cx="31" cy="31" r="30" fill="#e01f26"/><circle cx="31" cy="31" r="25" fill="none" stroke="#fff" stroke-width="1.5"/><path d="M17 36 L31 22 L45 36 M22 31 V42 H40 V31" fill="none" stroke="#fff" stroke-width="2.5"/></svg>Roof repairs</li>
    <li><svg class="icon" viewBox="0 0 62 62"><circle cx="31" cy="31" r="30" fill="#e01f26"/><circle cx="31" cy="31" r="25" fill="none" stroke="#fff" stroke-width="1.5"/><path d="M19 20 H43 V26 H19 Z M24 26 V44 M38 26 V40 M38 40 L33 44" fill="none" stroke="#fff" stroke-width="2.5"/></svg>Gutters systems</li>
    <li><svg class="icon" viewBox="0 0 62 62"><circle cx="31" cy="31" r="30" fill="#e01f26"/><circle cx="31" cy="31" r="25" fill="none" stroke="#fff" stroke-width="1.5"/><path d="M19 19 H43 V43 H19 Z M31 19 V43 M19 31 H43" fill="none" stroke="#fff" stroke-width="2.5"/></svg>Windows</li>
    <li><svg class="icon" viewBox="0 0 62 62"><circle cx="31" cy="31" r="30" fill="#e01f26"/><circle cx="31" cy="31" r="25" fill="none" stroke="#fff" stroke-width="1.5"/><path d="M20 20 H38 V28 H20 Z M38 24 H43 V33 H30 V37 M28 37 H32 V45 H28 Z" fill="none" stroke="#fff" stroke-width="2.5"/></svg>Painting interior/exterior</li>
    <li><svg class="icon" viewBox="0 0 62 62"><circle cx="31" cy="31" r="30" fill="#e01f26"/><circle cx="31" cy="31" r="25" fill="none" stroke="#fff" stroke-width="1.5"/><path d="M18 28 L31 18 L44 28 V44 H18 Z M18 34 H44 M18 39 H44" fill="none" stroke="#fff" stroke-width="2.5"/></svg>Siding</li>
  </ul>
  <div class="divider"></div>
  <div class="about">
    <p><strong>Main focus is roofing</strong> though! We do tons of door knocking to in area that are recently impacted by storms and offer free inspections to homeowner/property owners who are concerned or curious how their roof/property held up during the storm.</p>
    <p><strong>We also offer inspections</strong> with a Drone Inspections using SKYLOOM AI HAIL SCANNER SUITE for those people who just feel more comfortable with that.</p>
  </div>

  <div class="dark-foot"></div>
  <div class="photo one" role="img" aria-label="Craftsman style house with colourful front garden"></div>
  <div class="photo two" role="img" aria-label="Aerial view of a home with a new grey shingle roof"></div>
  <div class="photo three" role="img" aria-label="Brick house at dusk with a ladder against the roof"></div>

  <p class="foot-text">Main focus is roofing though! We do tons of door knocking to in area that are recently impacted by storms and offer free inspections to homeowner/property owners who are concerned or curious how their roof/property held up during the storm. We also offer inspections with a Drone Inspections using SKYLOOM AI HAIL SCANNER SUITE for those people who just feel more comfortable with that.</p>
  <svg class="award a" viewBox="0 0 111 111" role="img" aria-label="Manufacturer certification badge"><path d="M55.5 2 L109 55.5 L55.5 109 L2 55.5 Z" fill="#c9a44c"/><path d="M55.5 10 L101 55.5 L55.5 101 L10 55.5 Z" fill="#1c1c1e"/></svg>
  <svg class="award b" viewBox="0 0 111 111" role="img" aria-label="Manufacturer award badge"><path d="M55.5 2 L109 55.5 L55.5 109 L2 55.5 Z" fill="#c9a44c"/><path d="M55.5 10 L101 55.5 L55.5 101 L10 55.5 Z" fill="#2b3a5c"/></svg>
  <div class="rule"></div>
  <div class="contacts">
    <span><svg viewBox="0 0 24 24"><path d="M6.6 10.8a15 15 0 0 0 6.6 6.6l2.2-2.2c.3-.3.7-.4 1-.2 1.1.4 2.3.6 3.6.6.6 0 1 .4 1 1V20c0 .6-.4 1-1 1A17 17 0 0 1 3 4c0-.6.4-1 1-1h3.5c.6 0 1 .4 1 1 0 1.3.2 2.5.6 3.6.1.3 0 .7-.2 1z" fill="#e01f26"/></svg>(555) 014-2297</span>
    <span><svg viewBox="0 0 24 24"><path d="M2 5h20v14H2z" fill="#e01f26"/><path d="M2 5l10 8 10-8" fill="none" stroke="#1c1c1e" stroke-width="1.6"/></svg>info@velacrestga.com</span>
    <span><svg viewBox="0 0 24 24"><circle cx="12" cy="12" r="9.5" fill="none" stroke="#e01f26" stroke-width="2"/><path d="M2.5 12h19M12 2.5c3 3 3 16 0 19M12 2.5c-3 3-3 16 0 19" fill="none" stroke="#e01f26" stroke-width="1.6"/></svg>www.velacrestga.com</span>
  </div>
</main>
</body>
</html>
```